Short Stage Works Gala

I need a poster design for our 2012 play festival called 'The Harlow Brindle Gala of Short Stage Works 2012'. We are a community theatre in Port Macquarie, NSW, Australia. A beautiful seaside town with Norfolk Pine Trees and lots of pelicans. Our website is at www.lanternhousestage.org.au for more info. Our logo colours are a vibrant navy blue, red and yellow. The poster would need to depict drama, theatre, our logo, fun, and excitement. The dates are 8 - 10 June 2012. For more information e-mail m.r.dunmore@wavelink-mail.com

Target Market(s)

All age groups and people interested in theatre

Industry/Entity Type

Festival

Requirements
Must have
• Title - Harlow Brindle Gala of Short Stage Works
For more information e-mail m.r.dunmore@wavelink-mail.com
Dates - 8 - 10 June 2012
Lanternhouse Stage Logo
Website Address - www.lanternhousestage.org.au
Nice to have
• Background could include a picture of a theatrical stage

```html
<!DOCTYPE html>
<html lang="en">
<head>
<meta charset="utf-8">
<title>Harlow Brindle Gala of Short Stage Works 2012</title>
<link rel="stylesheet" href="https://fonts.googleapis.com/css2?family=Lato:wght@700;900&display=swap">
<style>
  :root {
    --festival-red: #d3252b;
    --festival-navy: #23215f;
    --festival-white: #ffffff;
    --festival-yellow: #f7e719;
  }
  html, body {
    margin: 0;
    padding: 0;
    overflow: hidden;
    background: var(--festival-white);
  }
  .poster {
    position: relative;
    width: 848px;
    height: 1200px;
    overflow: hidden;
    background: var(--festival-white);
    font-family: "Lato", "Helvetica Neue", Arial, sans-serif;
  }
  .poster-art {
    position: absolute;
    inset: 0;
    width: 848px;
    height: 1200px;
  }
  .panel { fill: var(--festival-red); }
  .title-line {
    font-family: "Lato", "Helvetica Neue", Arial, sans-serif;
    font-weight: 900;
    text-transform: uppercase;
  }
  .title-small { fill: var(--festival-navy); }
  .title-big { fill: var(--festival-white); }
  .event-dates {
    fill: var(--festival-navy);
    font-family: "Lato", "Helvetica Neue", Arial, sans-serif;
    font-weight: 900;
  }
  .info-band {
    position: absolute;
    left: 0;
    top: 1045px;
    width: 848px;
    height: 80px;
    background: var(--festival-navy);
    color: var(--festival-white);
  }
  .info-band__contact {
    position: absolute;
    right: 28px;
    top: 14px;
    margin: 0;
    font-size: 15px;
    font-weight: 700;
  }
  .info-band__web {
    position: absolute;
    right: 28px;
    top: 44px;
    margin: 0;
    font-size: 20px;
    font-weight: 700;
  }
  .org-mark {
    position: absolute;
    left: 40px;
    top: 1069px;
    display: flex;
    align-items: center;
    gap: 10px;
    color: var(--festival-white);
    font-size: 20px;
    font-weight: 900;
  }
  .org-mark__dot {
    width: 22px;
    height: 22px;
    border-radius: 50%;
    background: var(--festival-yellow);
  }
</style>
</head>
<body>
<main class="poster">
  <svg class="poster-art" viewBox="0 0 848 1200" xmlns="http://www.w3.org/2000/svg">
    <defs>
      <linearGradient id="pine-fade" x1="0" y1="0" x2="0" y2="1">
        <stop offset="0" stop-color="#d3252b" stop-opacity="0.55"/>
        <stop offset="1" stop-color="#d3252b" stop-opacity="1"/>
      </linearGradient>
    </defs>
    <path class="panel" d="M25 175 C 120 230 190 300 250 335 C 330 370 480 345 600 345 C 700 345 800 360 822 480 L 822 1172 L 25 1172 Z"/>
    <path role="img" aria-label="Silhouette of Norfolk pine trees on a hillside" fill="url(#pine-fade)"
          d="M0 20 L 60 0 L 330 0 Q 400 150 420 350 L 250 335 C 190 300 120 230 25 175 L 0 165 Z"/>
    <text class="title-line title-small" x="108" y="297" font-size="58" textLength="632" lengthAdjust="spacingAndGlyphs">Harlow Brindle</text>
    <text class="title-line title-small" x="108" y="400" font-size="96" textLength="634" lengthAdjust="spacingAndGlyphs">Gala of</text>
    <text class="title-line title-big" x="118" y="587" font-size="210" textLength="622" lengthAdjust="spacingAndGlyphs">Short</text>
    <text class="title-line title-big" x="118" y="772" font-size="205" textLength="622" lengthAdjust="spacingAndGlyphs">Stage</text>
    <text class="title-line title-big" x="112" y="882" font-size="128" textLength="630" lengthAdjust="spacingAndGlyphs">Works</text>
    <text class="event-dates" x="370" y="940" font-size="42" textLength="366" lengthAdjust="spacingAndGlyphs">8 - 10 JUNE 2012</text>
  </svg>

  <section class="info-band">
    <p class="info-band__contact">For more information e-mail m.r.dunmore@wavelink-mail.com</p>
    <p class="info-band__web">www.lanternhousestage.org.au</p>
  </section>

  <div class="org-mark">
    <span class="org-mark__dot"></span>
    <span class="org-mark__name">Lanternhouse Stage</span>
  </div>
</main>
</body>
</html>
```